Consultancy Business Card Design

We need a business card design for a new company based in singapore called FortyOne. FortyOne a boutique consultancy firm offering broad-based business solutions, from conception to re-invention, for ventures from new start-ups to long-running traditional businesses.
Its 2 main divisions (Food & Beverage Operations and Construction & Project Management) have access to a wide range of networks, knowledge bases, and resources to service its clients across numerous diverse sectors. This includes, and is not limited to, construction, F&B, and retail.
We are a company that combines the ambition, boldness and energy of one in the 20s with the dedication, level-headedness and dependability of one entering its 30s. Bridging the experiences of the old with ideals of the young, we draw on the positives of both to create a unique synergy.
We hope to see designs that fits our company profile.
Boutique
Contact Information for Business Card
FortyOne(Company Name)
Marcus Tan (Name)
Principle Consultant (Title)
F&B and Hospitality (Division)
(+65) 8364 5107 (Contact no.)
marcus@fortyone-example.com.sg (Email)
Colors
Designer to choose colors to be used in the design.

```html
<!DOCTYPE html>
<html lang="en">
<head>
<meta charset="utf-8">
<title>FortyOne Business Card</title>
<link href="https://fonts.googleapis.com/css2?family=Roboto:wght@400;900&display=swap" rel="stylesheet">
<style>
  :root {
    --paper: #ffffff;
    --ink: #000000;
    --crimson: #be1e2d;
    --sand: #c2b59b;
    --frame: #c9c9c9;
    --shadow: rgba(0, 0, 0, 0.35);
  }
  html, body {
    margin: 0;
    padding: 0;
    overflow: hidden;
  }
  body {
    width: 1200px;
    height: 1200px;
    background: var(--paper);
    font-family: "Roboto", Arial, sans-serif;
    position: relative;
  }
  .canvas-frame {
    position: absolute;
    inset: 0;
    border: 1px solid var(--frame);
    box-sizing: border-box;
  }
  .card {
    position: absolute;
    left: 332px;
    width: 544px;
    height: 329px;
    overflow: hidden;
    box-shadow: 6px 7px 6px var(--shadow);
  }
  .card svg.card-art {
    position: absolute;
    inset: 0;
    width: 100%;
    height: 100%;
  }
  .card-front {
    top: 204px;
    background: var(--paper);
    outline: 1px solid #e2e2e2;
  }
  .brand-name {
    position: absolute;
    left: 142px;
    top: 146px;
    margin: 0;
    font-weight: 900;
    font-size: 40px;
    letter-spacing: 0.5px;
    text-transform: uppercase;
    color: var(--ink);
    line-height: 1;
  }
  .card-back {
    top: 709px;
    background: var(--ink);
  }
  .contact {
    position: absolute;
    right: 38px;
    text-align: right;
    color: var(--ink);
  }
  .identity { top: 47px; }
  .person-name {
    margin: 0;
    font-size: 33px;
    font-weight: 400;
    line-height: 1.1;
  }
  .person-role {
    margin: 4px 0 0;
    font-size: 19px;
    line-height: 1.25;
  }
  .details {
    bottom: 32px;
    font-size: 19px;
    line-height: 1.38;
  }
  .details p { margin: 0; }
</style>
</head>
<body>
  <div class="canvas-frame"></div>

  <section class="card card-front">
    <svg class="card-art" viewBox="0 0 453 274" preserveAspectRatio="none" aria-hidden="true">
      <path fill="var(--sand)" d="M360,0 C410,30 405,95 372,155 C342,205 320,240 320,274 L453,274 L453,0 Z"/>
      <path fill="var(--ink)" d="M380,0 C422,40 418,105 392,162 C366,215 348,245 347,274 L453,274 L453,0 Z"/>
    </svg>
    <h1 class="brand-name">FortyOne</h1>
  </section>

  <section class="card card-back">
    <svg class="card-art" viewBox="0 0 453 274" preserveAspectRatio="none" aria-hidden="true">
      <path fill="var(--sand)" d="M88,0 C60,25 58,70 72,115 C92,175 128,225 128,274 L453,274 L453,0 Z"/>
      <path fill="var(--crimson)" d="M113,0 C85,22 82,65 97,112 C117,172 155,222 155,274 L453,274 L453,0 Z"/>
    </svg>
    <div class="contact identity">
      <h2 class="person-name">Marcus Tan</h2>
      <p class="person-role">Principal Consultant<br>F&amp;B and Hospitality</p>
    </div>
    <div class="contact details">
      <p class="phone">(+65) 8364 5107</p>
      <p class="email">marcus@fortyone-example.com.sg</p>
    </div>
  </section>
</body>
</html>
```